Business school needs a web design

Who We are:
KTRV is a small business school that offers programs in Project Management. The school is based in West Africa and welcomes students from the whole area. Our aim is to become one of the reference business schools in Africa.

Project Brief:
The site will include all informations relevant for different types of visitors that we have: actual and future students, companies, mass media, future employees, ect. It will present information about subscription, list of programs, presentation of the school and its team,etc.

What We want:
This competition is for Design only no coding! We need design for two pages.
We did some wireframing for the home page and the list of programs page. We made them just to show how we imagine the website would look like. But we encourage creative designs, so you don't have to stick to the wireframe models.

Sites We like:
http://www.larchmontgate.example/
http://www.pelvarin.example/fr/etudes.html
http://www.qwd.example/mba/Pages/default.aspx

Color schemes
The logo of the school is red and black. So the color scheme of the website should match that. For the rest, it is opened to your imagination.
Updates

The payment for the project is now garanteed. Good luck to you all !

Target Market(s)

The target market is diversified because we have students of different ages, also company representatives or employees that might visit the website for recruitment purposes. But the majority of our audience should be aged between 20 - 30 years.

Industry/Entity Type

Small Business

Requirements
Must have
• The design must include two pages: a home page and another interior page : might be the list of programs or any other page relevant to the domain. The Home page must include a slide show at the beginning.
The background page must be white.
Nice to have
• The use of flat design for this project is preferred.
The use of Twitter bootstrap as a base for the design is an asset.

```html
<!DOCTYPE html>
<html lang="fr">
<head>
<meta charset="utf-8">
<title>KTRV — École de management de projets</title>
<link href="https://fonts.googleapis.com/css2?family=Roboto+Condensed:wght@400;700&family=Arimo:ital,wght@0,400;0,700;1,400&display=swap" rel="stylesheet">
<style>
:root{
  --red:#d9534f;
  --teal:#45bfa4;
  --ink:#333;
  --text:#555;
  --muted:#888;
  --page:#e9e9e9;
  --header:#e3e3e3;
  --topbar:#3a3a3a;
  --footer:#2c2c2c;
  --rule:#666;
}
*{margin:0;padding:0;box-sizing:border-box}
html,body{width:1016px;height:1200px;overflow:hidden}
body{position:relative;background:var(--page);font-family:"Arimo",Arial,sans-serif;color:var(--text);font-size:9px;line-height:1.42}
.abs{position:absolute}
.cond{font-family:"Roboto Condensed","Arial Narrow",sans-serif}
a{color:inherit;text-decoration:none}
.more{color:var(--red);font-weight:700;font-size:8px;text-align:right}

/* top bar */
.topbar{left:0;top:0;width:1016px;height:16px;background:var(--topbar);color:#eee;font-size:8.5px}
.topbar .links{position:absolute;left:403px;top:2px;display:flex;gap:11px}
.search{position:absolute;left:708px;top:3px;width:90px;height:10px;background:#fff;color:#999;font-size:7px;padding-left:3px;line-height:10px}
.search-btn{position:absolute;left:797px;top:0;width:17px;height:16px;background:var(--red)}

/* header */
.header{left:0;top:16px;width:1016px;height:48px;background:var(--header)}
.logo{position:absolute;left:203px;top:14px;display:flex;align-items:center;gap:4px;font-family:"Roboto Condensed",sans-serif;font-weight:700;font-size:17px;color:var(--red)}
.logo i{display:block;width:12px;height:12px;border-radius:50%;background:var(--red)}
.nav{position:absolute;top:18px;font-weight:700;font-size:9.5px;color:#444}
.nav.active{border-bottom:1px solid #444;padding-bottom:1px}

/* slider */
.slide{left:0;top:64px;width:1016px;height:302px;background:linear-gradient(90deg,#4d4340 0%,#7a6360 25%,#b9625f 50%,#d46663 75%,#da6d6a 100%)}
.slide-box{left:458px;top:96px;width:311px;height:238px;background:rgba(140,70,70,.45);color:#fff;padding:4px 6px}
.slide-box h1{font-family:"Roboto Condensed",sans-serif;font-weight:700;font-size:33px;line-height:1.1;margin-bottom:16px}
.slide-box p{font-weight:700;font-size:8.8px;line-height:1.44;margin-bottom:12px;text-align:justify}
.arrow{top:198px}
.dots-band{left:0;top:366px;width:1016px;height:25px;background:#d98683}
.dot{top:375px;width:9px;height:9px;border-radius:50%;background:#eee}

/* section headings */
.h2{font-family:"Roboto Condensed",sans-serif;font-weight:700;font-size:14px;color:#333;line-height:1}
.h2 .r{color:var(--red)} .h2 .t{color:var(--teal)}
.rule{height:1px;background:var(--rule)}

/* left column */
.who{left:203px;top:413px;width:96px;height:126px;border:1px solid #bbb;border-top:none}
.who-title{left:207px;top:409px;background:var(--page);padding-right:4px;font-family:"Roboto Condensed",sans-serif;font-weight:700;font-size:8px;color:#333}
.who-top{left:252px;top:414px;width:47px;height:1px;background:#bbb}
.who ul{list-style:none;padding:15px 0 0 19px;font-size:8.8px;color:#444;line-height:15.2px}
.video{left:203px;top:601px;width:96px;height:97px;background:radial-gradient(circle at 50% 45%,#bbb 0%,#555 30%,#111 75%)}
.play{left:237px;top:640px;width:28px;height:20px;border:1px solid #ddd;background:rgba(40,40,40,.7)}
.newsletter-text{left:203px;top:771px;width:102px;font-size:8.8px;color:#444;text-align:justify}
.email{left:203px;top:843px;width:86px;height:16px;background:#fff;color:#888;font-style:italic;font-size:8.5px;padding:2px 4px}
.email-btn{left:290px;top:843px;width:15px;height:16px;background:var(--red)}

/* middle column */
.intro{left:330px;top:433px;width:300px;font-size:8.8px;color:#444;text-align:center}
.thumb{top:540px;width:95px;height:74px}
.post{top:619px;width:128px;font-size:8.5px;color:#888;font-style:italic;line-height:1.5}
.post b{color:#444}
.post .cat{color:var(--red);font-weight:700}
.post .by{font-style:normal;color:#666}
.post .by em{color:var(--red);font-weight:700}
.event-date{width:37px;height:34px;background:var(--teal);color:#fff;text-align:center}
.event-date .d{font-family:"Roboto Condensed",sans-serif;font-weight:700;font-size:17px;line-height:20px;color:#2b8f78}
.event-date .m{font-size:8px;line-height:10px}
.event-band{height:4px;background:#eee;width:37px}
.event{left:388px;width:243px}
.event h3{font-family:"Roboto Condensed",sans-serif;font-weight:700;font-size:11px;color:#444;margin-bottom:3px}
.event p{font-size:7px;color:#888;line-height:1.35}

/* right column */
.news{left:660px;width:153px;font-size:7.8px;color:#888;line-height:1.6}
.news .date{font-weight:700;font-size:8.5px;color:#444;margin-bottom:7px}
.news .icon{float:left;width:34px;height:24px;margin:5px 8px 2px 6px;background:#c9c9c9;transform:rotate(-12deg);border-radius:2px}
.news-sep{left:700px;width:113px;height:1px;background:#555}

/* partners */
.partners{left:203px;top:959px;width:611px;height:52px;border:2px solid #c5c5c5;background:#e2e2e2;display:flex;align-items:center;justify-content:space-around;padding:0 20px}
.partner{font-family:"Roboto Condensed",sans-serif;font-weight:700;font-size:18px;color:#6a6a6a}

/* footer */
.footer{left:0;top:1030px;width:1016px;height:154px;background:var(--footer);color:#fff;border-top:2px solid #ddd}
.f-col{top:1044px}
.f-col h4{font-family:"Roboto Condensed",sans-serif;font-weight:700;font-size:14px;line-height:1;padding-bottom:6px;border-bottom:1px solid #ccc;width:112px}
.f-col ul{list-style:none;margin-top:18px;font-weight:700;font-size:8.5px;line-height:16.2px}
.f-addr{font-weight:700;font-size:8.5px;line-height:12.5px;margin-top:18px}
.f-addr .big{font-size:10px}
.phone{display:flex;align-items:center;gap:10px;font-weight:700;font-size:10.5px;margin-top:6px}
.f-divider{left:673px;top:1080px;width:1px;height:82px;background:#ccc}
.social{top:1102px;width:26px;height:30px}
.copyright{left:0;top:1184px;width:1016px;height:16px;background:#555;color:#fff;font-weight:700;font-size:7.5px;text-align:center;line-height:16px;font-family:"Roboto Condensed",sans-serif}
</style>
</head>
<body>

<div class="abs topbar">
  <div class="links"><a href="#">Répertoire du personnel</a><a href="#">Blog</a><a href="#">Salle de presse</a><a href="#">Contact</a></div>
  <div class="search">Recherche</div>
  <div class="search-btn">
    <svg width="17" height="16" viewBox="0 0 17 16"><circle cx="7.5" cy="7" r="3.5" fill="none" stroke="#fff" stroke-width="1.4"/><line x1="10" y1="9.5" x2="13" y2="12.5" stroke="#fff" stroke-width="1.6"/></svg>
  </div>
</div>

<header class="abs header">
  <div class="logo"><i></i>KTRV</div>
  <a class="nav active" style="left:360px" href="#">KTRV</a>
  <a class="nav" style="left:407px" href="#">Programmes et formations</a>
  <a class="nav" style="left:556px" href="#">Etudiants</a>
  <a class="nav" style="left:621px" href="#">Nouvelles et évènements</a>
  <a class="nav" style="left:761px" href="#">Entreprises</a>
</header>

<section>
  <div class="abs slide" role="img" aria-label="Photo d'un enseignant face à un amphithéâtre d'étudiants, teintée de rouge"></div>
  <div class="abs slide-box">
    <h1>KTRV</h1>
    <p>Lorem ipsum dolor sit amet, consectetur adipiscing elit. Phasellus venenatis pellentesque aliquet. Fusce auctor est ut dolor dignissim, non tempor leo ornare. Sed eget tristique libero. Aliquam dapibus est ac eros consectetur, molestie placerat justo eleifend.</p>
    <p>Lorem ipsum dolor sit amet, consectetur adipiscing elit. Phasellus venenatis pellentesque aliquet. Fusce auctor est ut dolor dignissim, Fusce auctor est ut dolor dignissim, non tempor leo ornare. Sed eget tristique libero. Aliquam dapibus est ac eros consectetur, molestie placerat justo eleifend.</p>
    <p>Fusce auctor est ut dolor dignissim, non tempor leo ornare. Sed eget tristique libero. Aliquam dapibus est ac eros consectetur, molestie placerat justo eleifend.</p>
  </div>
  <svg class="abs arrow" style="left:202px" width="28" height="38" viewBox="0 0 28 38"><polyline points="24,2 4,19 24,36" fill="none" stroke="#eee" stroke-width="3"/></svg>
  <svg class="abs arrow" style="left:786px" width="28" height="38" viewBox="0 0 28 38"><polyline points="4,2 24,19 4,36" fill="none" stroke="#eee" stroke-width="3"/></svg>
  <div class="abs dots-band"></div>
  <div class="abs dot" style="left:489px"></div>
  <div class="abs dot" style="left:503px;background:#777"></div>
  <div class="abs dot" style="left:517px"></div>
</section>

<!-- left column -->
<aside>
  <div class="abs who"><ul>
    <li>Futur étudiant</li><li>Etudiant actuel</li><li>Entreprise</li><li style="text-decoration:underline">Employeur</li><li>Postulant</li><li>Médias</li><li>Partenaire</li>
  </ul></div>
  <div class="abs who-top"></div>
  <div class="abs who-title">VOUS ETES:</div>

  <div class="abs h2" style="left:203px;top:572px"><span class="r">KTRV</span>.tv</div>
  <div class="abs rule" style="left:203px;top:587px;width:102px"></div>
  <div class="abs video" role="img" aria-label="Aperçu vidéo d'une silhouette en contre-jour"></div>
  <div class="abs play"><svg width="26" height="18" viewBox="0 0 26 18"><polygon points="10,4 18,9 10,14" fill="#eee"/></svg></div>
  <div class="abs more" style="left:203px;top:709px;width:102px">+ de vidéos &gt;</div>

  <div class="abs h2" style="left:203px;top:748px;display:flex;align-items:center;gap:3px">
    <svg width="17" height="13" viewBox="0 0 17 13"><rect width="17" height="13" fill="#2a8f7a"/><polyline points="1,1 8.5,7 16,1" fill="none" stroke="#fff" stroke-width="1.3"/></svg>NEWSLETTER</div>
  <div class="abs rule" style="left:203px;top:764px;width:102px"></div>
  <p class="abs newsletter-text">Recevez les dernières nouvelles de l'KTRV, ainsi que des ressources utiles sur le management de projets.</p>
  <div class="abs email">E-mail...</div>
  <div class="abs email-btn"><svg width="15" height="16" viewBox="0 0 15 16"><polygon points="5,4 11,8 5,12" fill="#fff"/></svg></div>
</aside>

<!-- middle column -->
<main>
  <h2 class="abs h2" style="left:330px;top:410px"><span class="t">KTRV</span>: DEVENEZ LES GESTIONNAIRES DE DEMAIN</h2>
  <p class="abs intro">Lorem ipsum dolor sit amet, consectetur adipiscing elit. Vestibulum pretium orci vitae quam semper dapibus. Proin viverra, erat se d suscipit consectetur, ante arcu bibendum urna, et molestie elit elit nec purus. Sed a sollicitudin nisi. Nam tristique a metus eget tempus</p>

  <h2 class="abs h2" style="left:330px;top:511px;color:var(--teal)">BLOG</h2>
  <div class="abs rule" style="left:330px;top:527px;width:299px"></div>
  <div class="abs thumb" style="left:330px;background:radial-gradient(circle at 50% 50%,#cf5a5e 0,#cf5a5e 36px,#d6d2d0 37px)" role="img" aria-label="Visuel d'article de blog, cercle rouge sur fond gris"></div>
  <div class="abs thumb" style="left:508px;background:linear-gradient(135deg,#3b9e96,#7fc3bc 50%,#c9d0c8)" role="img" aria-label="Visuel d'article sur une lettre d'information de blog"></div>
  <div class="abs post" style="left:330px"><b>Nov 12, 2063:</b> <span class="cat">Outdoor</span><br>Lorem ipsum dolor sit amet, consectetur adipiscing elit. Vestibulum pretium orci vitae quam semper dapibus. Proin viverra.<br><span class="by">By <em>You</em></span></div>
  <div class="abs post" style="left:508px"><b>Nov 13, 2053:</b> <span class="cat">OMBlog</span><br>Lorem ipsum dolor sit amet, consectetur adipiscing elit. Vestibulum pretium orci vitae quam semper dapibus. Proin viverra.<br><span class="by">By <em>Us</em></span></div>
  <div class="abs more" style="left:330px;top:695px;width:121px">Lire la suite &gt;</div>
  <div class="abs more" style="left:508px;top:695px;width:121px">Lire la suite &gt;</div>

  <h2 class="abs h2" style="left:330px;top:735px;color:var(--red)">EVENEMENTS</h2>
  <div class="abs rule" style="left:330px;top:750px;width:299px"></div>

  <div class="abs event-band" style="left:334px;top:764px"></div>
  <div class="abs event-date" style="left:334px;top:768px"><div class="d">12</div><div class="m">Nov</div></div>
  <div class="abs event" style="top:762px"><h3>Ipsum dalius</h3><p>Etiam tortor leo, euismod quis est in, convallis bibendum ante. Ut consequat justo mi, eget bibendum orci consectetur tincidunt. Fusce id nunc interdum, accumsan elit in, porttitor erat.</p></div>

  <div class="abs event-band" style="left:334px;top:817px"></div>
  <div class="abs event-date" style="left:334px;top:821px"><div class="d">03</div><div class="m">Mars</div></div>
  <div class="abs event" style="top:818px"><h3>Dalius ipsum</h3><p>Etiam tortor leo, euismod quis est in, convallis bibendum ante. Ut consequat justo mi, eget bibendum orci consectetur tincidunt. Fusce id nunc interdum, accumsan elit in, porttitor erat.</p></div>
  <div class="abs more" style="left:480px;top:867px;width:149px;font-size:8.5px">Tout les évènements &gt;</div>
</main>

<!-- right column -->
<aside>
  <h2 class="abs h2" style="left:660px;top:410px">DERNIERES <span class="t">NOUVELLES</span>:</h2>
  <div class="abs rule" style="left:660px;top:426px;width:153px"></div>

  <div class="abs news" style="top:432px"><div class="date">10 Novembre 2042</div><span class="icon"></span>Proin ac sem arcu. Mauris id urna a dolor varius commodo. Nam placerat, par oc maris de velit quis dignissim eleifend, dolor arcu ultricies justo, vitae auctor dui massa quis ante. Donec ut nisl a nisi ullamcorper ullamcorper eu eu nibh.<div class="more">Lire la suite &gt;</div></div>
  <div class="abs news-sep" style="top:569px"></div>

  <div class="abs news" style="top:581px"><div class="date">03 Décembre 2021</div><span class="icon"></span>Proin ac sem arcu. Mauris id urna a dolor varius commodo. Nam placerat, par oc maris de velit quis dignissim eleifend, dolor arcu ultricies justo, vitae auctor dui massa quis ante. Donec ut nisl a nisi ullamcorper ullamcorper eu eu nibh.<div class="more">Lire la suite &gt;</div></div>
  <div class="abs news-sep" style="top:718px"></div>

  <div class="abs news" style="top:730px"><div class="date">23 Mars 2002</div><span class="icon"></span>Proin ac sem arcu. Mauris id urna a dolor varius commodo. Nam placerat, par oc maris de velit quis dignissim eleifend.<div class="more">Lire la suite &gt;</div></div>
  <div class="abs news-sep" style="top:828px"></div>

  <div class="abs news" style="top:840px"><div class="date">12 Janvier 1998</div><span class="icon"></span>Proin ac sem arcu. Mauris id urna a dolor varius commodo. Nam placerat, par oc maris de velit quis dignissim eleifend.<div class="more">Lire la suite &gt;</div></div>
</aside>

<div class="abs partners">
  <span class="partner">Valtoria</span>
  <span class="partner">Norvenne</span>
  <span class="partner">Brelmont</span>
  <span class="partner">Quissa</span>
  <span class="partner">Dunmara</span>
</div>

<footer>
  <div class="abs footer"></div>
  <div class="abs f-col" style="left:203px"><h4>A PROPOS</h4><ul><li>KTRV</li><li>Admissions</li><li>Calendrier de l'école</li><li>Offres d'emplois</li><li>Répertoire du personnel</li></ul></div>
  <div class="abs f-col" style="left:362px"><h4>ETUDIANTS</h4><ul><li>Accueil - Etudiants</li><li>Programmes et formations</li><li>Vie étudiante</li><li>Entreprises</li><li>Blog</li></ul></div>
  <div class="abs f-col" style="left:514px"><h4 style="color:var(--red)">KTRV</h4>
    <div class="f-addr"><div class="big">14, RUE DES BAOBABS</div>Près du grand marché de la<br>corniche ouest</div>
    <div class="phone" style="margin-top:12px"><svg width="13" height="13" viewBox="0 0 13 13"><path d="M3 1 L5 4 L4 5.5 Q5.5 8 7.5 9 L9 8 L12 10 L10.5 12 Q5 11.5 1 3 Z" fill="#fff"/></svg>( 000 ) 55 410 22 87</div>
    <div class="phone"><svg width="13" height="13" viewBox="0 0 13 13"><path d="M3 1 L5 4 L4 5.5 Q5.5 8 7.5 9 L9 8 L12 10 L10.5 12 Q5 11.5 1 3 Z" fill="#fff"/></svg>( 000 ) 55 410 22 87</div>
  </div>
  <div class="abs f-divider"></div>
  <div class="abs f-col" style="left:699px"><h4 style="color:var(--teal);text-align:right;width:114px">SUIVEZ-NOUS</h4></div>
  <div class="abs social" style="left:699px;background:#2f5b9c"></div>
  <div class="abs social" style="left:727px;background:#2aa2d6"></div>
  <div class="abs social" style="left:755px;background:#d33b35"></div>
  <div class="abs social" style="left:783px;background:#1f77a8"></div>
  <div class="abs copyright">Tous droits réservés © KTRV 2014</div>
</footer>

</body>
</html>
```